Online Advertising agency with fun music culture twist

We need a new website for our online advertising agency. The current site is just a placeholder but you can pull the text from the site- quillmarketbench.com. The new site will be 10 total pages. The current site has 8 pages. So this project will require the design and code for all 10 pages.

Things I like- Clean, easy to read, custom graphics, video,
splash 1-2 colors, futuristic, music twist, fun, interesting, looks amazing on a mobile site, extremely professional design.

Things I don't like- I hate stock graphics, pages that scroll to much, to many colors (rainbow), sites that don't flow, very templated cookie cutter sites, not mobile compliant.

We built a sophisticated buying platform for advertisers to reach the right person on the right device at the right time. I used to be a concert promoter and I have several musicians that work with us. We want to play into the fun and excitement of live music with an advertising twist hence the name Quill. We don't want to make it seem like a music company but we can use subtle vinyl and music references. My other company is meadowpixelworks.com for reference. I really like to design of my other company.

Target Market(s)

Online websites and fortune 500 advertisers- You can see my other company at meadowpixelworks.com

Industry/Entity Type

Advertising

Coding

Coded - Design and coding required

Number of Pages Required

5+ page

Font styles to use
Other font styles liked:
• Be creative

Requirements
Must have
• HTML5, Clean, easy to read, custom graphics, use of video graphics,
• splash 1-2 colors, futuristic, music twist, fun, interesting, looks amazing on a mobile site, extremely professional design. Play into the music theme, vinyl records etc
Nice to have
• Video, interactivity, custom build (not a template)
Should not have
• Flash. I hate stock photos, pages that scroll to much, to many colors (rainbow), sites that don't flow, very templated cookie cutter sites, not mobile compliant.

```html
<!DOCTYPE html>
<html lang="en">
<head>
<meta charset="utf-8">
<title>Quill Trading Desk</title>
<link rel="stylesheet" href="https://fonts.googleapis.com/css2?family=Lato:wght@400;700;900&display=swap">
<style>
:root{
  --ink:#111111;
  --gold:#f5b90f;
  --hero-light:#464648;
  --hero-dark:#303032;
  --paper:#f1f1f1;
  --text:#6a6a6a;
  --white:#ffffff;
  --icon:#555555;
}
*{margin:0;padding:0;box-sizing:border-box}
html,body{width:879px;height:1200px;overflow:hidden}
body{font-family:'Lato',sans-serif;background:var(--paper);position:relative}
.site-header{position:absolute;left:0;top:0;width:879px;height:80px;background:var(--ink);border-bottom:3px solid var(--gold)}
.brand{position:absolute;left:76px;top:20px;display:flex;align-items:center;gap:10px;color:#cfcfcf;font-weight:900;font-size:36px;letter-spacing:2px}
.brand-dot{width:12px;height:12px;border-radius:50%;background:#cfcfcf}
.account{position:absolute;right:75px;top:16px;display:flex;align-items:center;gap:18px;font-weight:700;font-size:11.5px;letter-spacing:.6px;color:var(--white)}
.btn-start{background:var(--gold);color:var(--ink);padding:6px 12px}
.main-nav{position:absolute;right:75px;top:55px;display:flex;gap:22px;font-weight:700;font-size:11.5px;letter-spacing:.6px;color:var(--white)}
.main-nav .active{color:var(--gold)}
.hero{position:absolute;left:0;top:80px;width:879px;height:391px;background:linear-gradient(var(--hero-light),var(--hero-dark))}
.hero-art{position:absolute;inset:0;background:radial-gradient(ellipse 230px 200px at 415px 215px,#1c1c1c 0%,#242424 70%,rgba(48,48,50,0) 100%)}
.hero-copy{position:absolute;left:0;top:134px;width:879px;text-align:center;color:var(--white)}
.hero-copy h1{color:var(--gold);font-weight:900;font-size:22px;letter-spacing:1px}
.hero-rule{display:block;margin:6px auto 10px}
.hero-copy p{font-weight:700;font-size:11.5px;line-height:16px}
.side-tab{position:absolute;left:817px;top:435px;width:62px;height:66px;background:var(--gold);border:1px solid #999}
.difference{position:absolute;left:77px;top:500px;width:731px;color:var(--text)}
.difference h2{color:var(--ink);font-weight:900;font-size:23px;letter-spacing:.5px;margin-bottom:16px}
.difference h3{color:var(--gold);font-weight:700;font-size:13.5px;margin:0 0 7px;letter-spacing:.2px}
.difference p{font-weight:700;font-size:11.4px;line-height:16.3px;letter-spacing:.15px;margin-bottom:12px;text-align:justify}
.difference p.last{margin-bottom:22px}
.contact{position:absolute;left:0;top:1021px;width:879px;height:141px;background:var(--white);border-top:3px solid var(--gold);text-align:center;color:var(--text)}
.contact h4{color:var(--ink);font-weight:900;font-size:18px;letter-spacing:1px;margin-top:41px}
.contact-line{display:flex;justify-content:center;align-items:center;gap:8px;font-weight:700;font-size:13px;letter-spacing:.4px;margin-top:8px}
.site-footer{position:absolute;left:0;top:1162px;width:879px;height:38px;background:var(--ink);color:var(--white)}
.copyright{position:absolute;left:70px;top:12px;font-weight:700;font-size:11.5px}
.social{position:absolute;right:72px;top:8px;display:flex;gap:7px}
.social span{width:21px;height:21px;border-radius:50%;background:var(--icon)}
</style>
</head>
<body>
<header class="site-header">
  <div class="brand"><span class="brand-dot"></span>QUILL</div>
  <div class="account"><span>SIGN UP / LOGIN</span><span class="btn-start">GET STARTED</span></div>
  <nav class="main-nav"><span class="active">HOME</span><span>ABOUT US</span><span>ADVERTISERS</span><span>PUBLISHERS</span><span>CONTACT US</span></nav>
</header>

<section class="hero">
  <div class="hero-art" role="img" aria-label="Illustration of a vinyl record spinning on a turntable with its tone arm"></div>
  <div class="hero-copy">
    <h1>WHY US</h1>
    <svg class="hero-rule" width="98" height="14" viewBox="0 0 98 14"><line x1="0" y1="7" x2="98" y2="7" stroke="#f5b90f" stroke-width="2"/><circle cx="47" cy="7" r="6.5" fill="#f5b90f"/></svg>
    <p>Our technology and services enable marketers to connect with the audiences they<br>want at the scale they need to achieve the outcomes they desire.</p>
  </div>
</section>
<div class="side-tab"></div>

<main class="difference">
  <h2>THE QUILL DIFFERENCE</h2>
  <h3>SIMPLICITY, EFFECTIVENESS &amp; ACCOUNTABILITY AT SCALE.</h3>
  <p class="last">You spend millions of dollars on digital media, and it’s become a complex, opaque part of your business. But it doesn’t have to be. Quill gives advertisers complete control of their digital ad spend through a fully transparent advertiser owned system. We dramatically streamline the digital marketing value chain, saving advertisers millions in fees and margins.</p>
  <h3>ENJOY TRANSPARENT MEDIA BUYING AT SCALE.</h3>
  <p>It’s your money, so you should know how it’s spent, where your campaigns are running, where they are working and even where they aren’t.</p>
  <p class="last">We can handle all of your digital media buying–from premium partners to reach-based programmatic buying–around the globe. Whether we do the work for you or you or a partner manages the campaigns, never worry about a black box managing your money again.</p>
  <h3>SIGNIFICANTLY INCREASE ROI AS A RESULT.</h3>
  <p class="last">You’ll see how much more value you can get from your digital media budget when you have a transparent, closed-loop system aligned to your needs. Once you eliminate waste, your additional budget can go towards real ads seen by real people. Imagine the performance improvements.Type your paragraph here.</p>
  <h3>STREAMLINE YOUR SUPPLY CHAIN.</h3>
  <p>In most other areas of marketing (such as email, CRM or your website), you’ve picked a vendor (or two) and created a close partnership. The same is now possible with digital media buying.</p>
  <p>Too many vendors create a lot of waste as they employ all sorts of tactics to bid against one another and take credit for online behavior that they didn’t cause. ClearBid Systems is enterprise technology that gives you the benefits of integrated capabilities with less waste.</p>
</main>

<section class="contact">
  <h4>COMPANYNAME INC.</h4>
  <div class="contact-line">
    <svg width="20" height="20" viewBox="0 0 20 20"><circle cx="10" cy="10" r="8.5" fill="none" stroke="#6a6a6a" stroke-width="2"/><path d="M6 6l3 2-1 3 3 2v3M12 4l1 3 3 1" fill="none" stroke="#6a6a6a" stroke-width="1.6"/></svg>
    <span>418 Harlow Ave, Boulder, CO 80302</span>
  </div>
  <div class="contact-line">
    <svg width="16" height="16" viewBox="0 0 16 16"><path d="M4 1h3l1 4-2 1.5c1 2 2.5 3.5 4.5 4.5L12 9l4 1v3c0 1-1 2-2 2C7 15 1 9 1 3c0-1 1-2 3-2z" fill="#6a6a6a"/></svg>
    <span>(555) 0142-7730</span>
  </div>
</section>

<footer class="site-footer">
  <div class="copyright">© QUILL 2016.</div>
  <div class="social"><span></span><span></span><span></span><span></span><span></span></div>
</footer>
</body>
</html>
```